SANDSTONE TRAIL TOURS Eye-catching design for A-frame sign (tour company Lightning Ridge - Australia)

We would need a simple but eye-catching design for our A-frame sign. The size of the sign is 595mm x 895mm. These signs stand on the curbside/outside various reception areas of motels and caravan parks here in Lightning Ridge. The aim is to make people book one of our tours. We have a design from previous years but there is too much info/words on there and it is hard to read. So we would like the new sign to be (quite) different. The base color should be black or dark. We don’t think we want big pictures on the sign but possibly the opal picture can somehow be integrated. This is only a though and not a must and we also are open to suggestion. The background can be one or more colors - solid or possibly different shades of it!?

I will attach an image of our current sign and of the sign of our competitor "Red Gum Excursions". We really like their sign and I have attached an image of it. Another image shows how the sign situation currently is. There are some places where only our signs is there but at most places it is in line with others.

We are a small family owned and operated tour operator in the outback of Australia. We are famous for precious black opals (just in case you don’t know but they are not black but very bright and colorful on the facing side:-). This is why most tourists come to Lightning Ridge to see our multi-cultural community, the opal mines and our very rare, precious and world-famous black opal.
Thanks a lot in advance for your interest and for your time to do a design for us here Down Under:-)

Target Market(s)

Grey nomads (pensioner), Families and young couples (oversea travellers)

Industry/Entity Type

Tourism

Font styles to use
Sans Serif

Colors

Designer to choose colors to be used in the design.

Requirements
Must have
• Our logo and the following info attached on word document.
Nice to have
• Please see description for this:-)
Should not have
• -Too small print
• -too crowded

```html
<!DOCTYPE html>
<html lang="en">
<head>
<meta charset="utf-8">
<title>Sandstone Trail Tours – A-frame sign</title>
<link rel="stylesheet" href="https://fonts.googleapis.com/css2?family=Montserrat:wght@600&family=Oswald:wght@400;500&display=swap">
<style>
  :root {
    --page: #ffffff;
    --board: #353433;
    --gold: #f7d233;
    --white: #ffffff;
    --red: #cf2f35;
    --green: #376539;
    --purple: #3f2a6b;
    --band: #f7e600;
    --ink: #1f1a17;
    --url-red: #c4121a;
  }
  html, body {
    margin: 0; padding: 0;
    width: 1200px; height: 1200px;
    overflow: hidden;
    background: var(--page);
  }
  .sign {
    position: absolute;
    left: 210px; top: 15px;
    width: 780px; height: 1170px;
    background: var(--board);
    overflow: hidden;
    font-family: "Oswald", "Arial Narrow", sans-serif;
  }
  .sign__decor { position: absolute; inset: 0; }
  .brand {
    position: absolute; left: 70px; top: 40px;
    display: flex; align-items: center; gap: 36px;
  }
  .brand__dot {
    width: 190px; height: 190px; border-radius: 50%;
    background: var(--gold);
  }
  .brand__text {
    font-family: "Montserrat", Arial, sans-serif;
    font-weight: 600;
    color: var(--gold);
  }
  .brand__name { font-size: 50px; line-height: 1.05; margin: 0; }
  .brand__rule { height: 3px; background: var(--gold); margin: 18px 0 12px; width: 330px; }
  .brand__place { font-size: 30px; margin: 0; }
  .ribbon {
    position: absolute;
    color: var(--white);
    text-align: center;
    font-size: 40px; line-height: 1.1;
    padding: 16px 30px;
    box-shadow: 0 8px 14px rgba(0,0,0,.35);
  }
  .ribbon em { font-style: normal; color: var(--gold); }
  .ribbon--town { background: var(--red); left: 255px; top: 330px; width: 370px; transform: rotate(-5deg); z-index: 1; }
  .ribbon--day { background: var(--green); left: 225px; top: 465px; width: 390px; transform: rotate(-6deg); z-index: 2; }
  .ribbon--evening { background: var(--purple); left: 325px; top: 640px; width: 340px; transform: rotate(-6deg); z-index: 3; }
  .slogan {
    position: absolute; left: 240px; top: 790px; width: 340px; margin: 0;
    text-align: center; color: var(--white);
    font-size: 40px; line-height: 1.12;
    transform: rotate(-6deg);
  }
  .slogan em { font-style: normal; color: var(--gold); font-size: 48px; }
  .book-now {
    position: absolute; left: 570px; top: 800px;
    width: 160px; height: 160px; border-radius: 50%;
    background: radial-gradient(circle at 40% 35%, #e5262c, #b10d14);
    border: 5px solid var(--white);
    box-shadow: 0 0 0 3px #b10d14;
    color: var(--white);
    display: flex; align-items: center; justify-content: center;
    text-align: center; font-size: 52px; line-height: .95; font-weight: 500;
    transform: rotate(-6deg);
    z-index: 5;
  }
  .contact {
    position: absolute; left: 60px; right: 30px; top: 1010px; height: 110px;
    background: var(--band); border-radius: 16px;
    transform: rotate(-5deg);
    display: flex; flex-direction: column; align-items: center; justify-content: center;
    z-index: 4;
  }
  .contact__phone {
    display: flex; align-items: center; gap: 12px;
    font-size: 46px; font-weight: 500; color: var(--ink); line-height: 1;
  }
  .contact__web { font-size: 34px; font-weight: 500; color: var(--ink); line-height: 1.15; }
  .contact__web span { color: var(--url-red); }
</style>
</head>
<body>
  <main class="sign">
    <svg class="sign__decor" width="780" height="1170" viewBox="0 0 780 1170">
      <defs>
        <linearGradient id="opal-left" x1="0" y1="0" x2="0" y2="1">
          <stop offset="0" stop-color="#d8322f"/>
          <stop offset=".3" stop-color="#e65d2c"/>
          <stop offset=".5" stop-color="#f6c92a"/>
          <stop offset=".75" stop-color="#7aa23a"/>
          <stop offset="1" stop-color="#1f5a24"/>
        </linearGradient>
        <linearGradient id="opal-right" x1="0" y1="0" x2="0" y2="1">
          <stop offset="0" stop-color="#5a2f8f"/>
          <stop offset=".35" stop-color="#3b2c78"/>
          <stop offset=".55" stop-color="#f35fd0"/>
          <stop offset="1" stop-color="#d8232a"/>
        </linearGradient>
      </defs>
      <g role="img" aria-label="Colourful opal pattern, left side">
        <path d="M0 300 Q200 520 160 1000 L0 1000 Z" fill="url(#opal-left)"/>
      </g>
      <path d="M0 275 Q225 510 185 1010" fill="none" stroke="#f7d233" stroke-width="3"/>
      <g role="img" aria-label="Colourful opal pattern, right side">
        <path d="M780 300 Q620 560 760 900 L780 900 Z" fill="url(#opal-right)"/>
      </g>
      <path d="M770 280 Q590 560 740 920" fill="none" stroke="#f7d233" stroke-width="3"/>
    </svg>

    <header class="brand">
      <div class="brand__dot"></div>
      <div class="brand__text">
        <p class="brand__name">SANDSTONE<br>TRAIL TOURS</p>
        <div class="brand__rule"></div>
        <p class="brand__place">LIGHTNING RIDGE</p>
      </div>
    </header>

    <div class="ribbon ribbon--town">The Ridge <em>TOWN TOUR</em><br>daily 9am &amp; 2pm</div>
    <div class="ribbon ribbon--day"><em>FULL DAY TOUR</em><br>to the opal fields &amp;<br>all bush pubs</div>
    <div class="ribbon ribbon--evening"><em>EVENING TOUR</em><br>Group &amp; Private Tours</div>

    <p class="slogan"><em>REAL TOURS</em><br>by locals for the<br><em>REAL EXPERIENCE</em></p>

    <div class="book-now">BOOK<br>NOW</div>

    <footer class="contact">
      <div class="contact__phone">
        <svg width="36" height="36" viewBox="0 0 24 24" aria-hidden="true">
          <circle cx="12" cy="12" r="12" fill="#c4121a"/>
          <path d="M8.6 6.5l1.6 2.6-1 1.2c.7 1.6 1.9 2.8 3.5 3.5l1.2-1 2.6 1.6-.6 2.1c-4.8-.3-8.5-4-8.8-8.8z" fill="#fff"/>
        </svg>
        02 5550 1234
      </div>
      <div class="contact__web"><span>WWW.</span>SANDSTONETRAILTOURS<span>.COM.AU</span></div>
    </footer>
  </main>
</body>
</html>
```